Exercise Physiologist needs business cards

I have a logo, I need business cards (Sole trader) as I am moving to a new location and would like an updated look. I provide gym based exercise rehabilitation, injury prevention and movement assessments. I have over 13 years experience as an Exercise Physiologist. I would like the cards to look professional but not boring and can be a little different to stand out when sitting with other Allied Health Professional cards.

Target Market(s)

GP's, Allied health practitioners, people with injuries wanting to exercise

Industry/Entity Type

Health And Wellness

Contact Information for Business Card

Megan Dorrit - Exercise Physiologist 0437 582 906
14 Larkspur Bend Rd
Westmere Heights
(Gate 5, Brannock Fitness)
vantorahealth@maildrop-example.com
socialpage-example.com/Vantora

Requirements
Must have
• I would like to include a section to add next appointment date and time space to the back of the card.
Nice to have
• Rounded corners and a black background on 1 or 2 sides.
Should not have
• Pictures of fit/toned bodies etc

```html
<!DOCTYPE html>
<html lang="en">
<head>
<meta charset="utf-8">
<title>Megan Dorrit – Business Card</title>
<link href="https://fonts.googleapis.com/css2?family=Lato:wght@400;700&display=swap" rel="stylesheet">
<style>
  :root {
    --blue-deep: #0a5fc2;
    --blue-light: #5eb0e0;
    --card-white: #f4f4f4;
    --ink: #333b44;
    --ink-soft: #6a7078;
    --backdrop: #e6e8eb;
  }
  * { box-sizing: border-box; margin: 0; padding: 0; }
  html, body {
    width: 1200px; height: 900px; overflow: hidden;
    background: var(--backdrop);
    font-family: "Lato", sans-serif;
  }
  .stage {
    width: 1200px; height: 900px;
    display: flex; align-items: center; justify-content: center; gap: 40px;
  }
  .card {
    position: relative;
    width: 540px; height: 330px;
    border-radius: 6px;
    overflow: hidden;
    background: var(--card-white);
    box-shadow: 0 8px 24px rgba(0,0,0,0.18);
  }

  /* Appointment side */
  .appt-header {
    height: 78px; background: var(--blue-deep); color: #fff;
    display: flex; align-items: center; justify-content: center;
    font-size: 22px; font-weight: 700; letter-spacing: 0.3px;
  }
  .appt-body { height: 142px; background: #fff; padding: 30px 34px 0; color: var(--ink-soft); }
  .appt-line { display: flex; align-items: flex-end; font-size: 17px; font-weight: 700; gap: 8px; }
  .appt-dots { flex: 1; border-bottom: 2px dotted var(--ink-soft); height: 14px; }
  .appt-days { display: flex; justify-content: space-between; margin-top: 30px; }
  .day { display: flex; align-items: center; gap: 7px; font-size: 15px; font-weight: 700; }
  .day-box { width: 18px; height: 18px; border: 2px solid var(--ink-soft); border-radius: 2px; background: #fff; }
  .appt-footer {
    height: 110px; background: var(--blue-light); color: #fff;
    display: flex; align-items: center; justify-content: center;
    font-size: 17px; font-weight: 700;
  }

  /* Contact side */
  .wave { position: absolute; left: 0; bottom: 0; width: 540px; height: 330px; }
  .person { position: absolute; left: 40px; top: 52px; }
  .person-name { color: var(--blue-deep); font-size: 21px; font-weight: 700; letter-spacing: 0.5px; }
  .person-role { color: var(--ink); font-size: 16px; }
  .brand { position: absolute; right: 34px; top: 40px; display: flex; align-items: center; gap: 10px; }
  .brand-mark { width: 58px; height: 58px; border-radius: 50%; background: var(--blue-deep); }
  .brand-name { color: var(--blue-deep); font-size: 26px; font-weight: 700; line-height: 1.1; }
  .brand-name small { display: block; font-size: 11px; letter-spacing: 1px; text-transform: uppercase; }
  .contact { position: absolute; left: 40px; top: 150px; color: var(--ink); font-size: 16px; line-height: 1.35; }
  .contact-phone { font-size: 18px; margin-bottom: 8px; }
  .contact-phone b { color: var(--blue-deep); }
</style>
</head>
<body>
<main class="stage">

  <section class="card card-appointment">
    <div class="appt-header">Your Next Appointment on</div>
    <div class="appt-body">
      <div class="appt-line">
        <span>Date :</span><span class="appt-dots"></span>
        <span>Time :</span><span class="appt-dots"></span>
        <span>AM / PM</span>
      </div>
      <div class="appt-days">
        <span class="day"><span class="day-box"></span>MON</span>
        <span class="day"><span class="day-box"></span>TUE</span>
        <span class="day"><span class="day-box"></span>WED</span>
        <span class="day"><span class="day-box"></span>THU</span>
        <span class="day"><span class="day-box"></span>FRI</span>
        <span class="day"><span class="day-box"></span>SAT</span>
      </div>
    </div>
    <div class="appt-footer">If unable to keep appointment, kindly give 24hrs notice.</div>
  </section>

  <section class="card card-contact">
    <svg class="wave" viewBox="0 0 540 330" aria-hidden="true">
      <path d="M0 248 C 120 300, 300 270, 540 150 L540 330 L0 330 Z" fill="var(--blue-light)"/>
      <path d="M0 256 C 130 302, 310 278, 540 162 L540 330 L0 330 Z" fill="var(--card-white)"/>
      <path d="M0 266 C 150 306, 330 284, 540 172 L540 330 L0 330 Z" fill="var(--blue-deep)"/>
    </svg>
    <div class="person">
      <div class="person-name">MEGAN DORRIT</div>
      <div class="person-role">Exercise Physiologist</div>
    </div>
    <div class="brand">
      <span class="brand-mark"></span>
      <span class="brand-name">vantora<small>Health &amp; Rehabilitation</small></span>
    </div>
    <div class="contact">
      <div class="contact-phone"><b>P:</b> 0437 582 906</div>
      <div>14 Larkspur Bend Rd</div>
      <div>Westmere Heights</div>
      <div>(Gate 5, Brannock Fitness)</div>
    </div>
  </section>

</main>
</body>
</html>
```